Cat-products company needs smart, yet endearing, business card

We need a business card design for a new, but up-and-running, business based in Honolulu, Hawaii. The business is Purrlane Nest Co. Our first product is the most environmentally-friendly cat grass kit ever seen on the planet. Future products, currently in the R&D phase, will include a variety of exciting cat scratchers. We also do consulting work to help apartment-dwellers make their home more cat-friendly and, in the future, plan on doing full, custom installs of structure to create high walkways for cats.

Target Market(s)

Middle-aged, apartment-dwelling, middle-class workers who own 1 or more cats and who dote on them.

Industry/Entity Type

Pet Care

Contact Information for Business Card

A striking, professional, yet warm and friendly design is what we're after.

Font styles to use
Serif
Sans Serif
Other font styles liked:
• Comfortaa

Colors

Designer to choose colors to be used in the design.

Requirements
Must have
• The company logo: (see attachment)
• The company name: Purrlane Nest Co
• The web address: www.purrlanenestco.example
• Email: support@purrlanenestco.example
• Phone: +1 (808) 555 0172
• Update (Fri Jun 30 3017 7:45pm Hawaii Time) I would like, is possible, uploaded picture of the cat grass kit on the back of the card with some text along the lines of: Purrlane Nest Co - Where The Freshest Kitty Sprouts Begin
Nice to have
• A cat picture, cartoon, real or silhouette that illustrates cats in action and/or relaxing; ie using the apartment space to live, play and relax in and being well-contented.
• Most of the website is done in the font: Comfortaa. It might be nice to continue using this for brand consistency.
Should not have
• Hard-to-read fonts.

```html
<!DOCTYPE html>
<html lang="en">
<head>
<meta charset="UTF-8">
<title>Purrlane Nest Co — Business Card</title>
<link href="https://fonts.googleapis.com/css2?family=Comfortaa:wght@500;700&display=swap" rel="stylesheet">
<style>
  :root {
    --marigold: #fbaa12;
    --cocoa: #45292a;
    --paper: #ffffff;
    --meadow: #3f8f2a;
    --meadow-light: #7cc24a;
    --soil: #2f2a26;
    --ginger: #c8702e;
  }
  * { margin: 0; padding: 0; box-sizing: border-box; }
  html, body {
    width: 1200px; height: 1200px; overflow: hidden;
    background: var(--paper);
    font-family: "Comfortaa", sans-serif;
  }
  .canvas { position: relative; width: 1200px; height: 1200px; }

  .card { position: absolute; left: 181px; width: 840px; height: 480px; overflow: hidden; }

  /* Front */
  .card--front { top: 88px; background: var(--marigold); color: var(--cocoa); }
  .brand-badge {
    position: absolute; left: 211px; top: 32px; width: 137px; height: 143px;
    background: var(--paper); border-radius: 12px;
    display: flex; align-items: center; justify-content: center; text-align: center;
  }
  .brand-badge__name { font-weight: 700; font-size: 22px; line-height: 1.15; color: var(--cocoa); }
  .company-name {
    position: absolute; left: 31px; top: 194px;
    font-weight: 700; font-size: 50px; letter-spacing: -1px; white-space: nowrap;
  }
  .contact { position: absolute; left: 29px; top: 270px; list-style: none; font-weight: 500; font-size: 24px; }
  .contact li { height: 40px; line-height: 30px; white-space: nowrap; }
  .cat-figure {
    position: absolute; left: 600px; top: 172px; width: 200px; height: 234px;
    background: var(--paper); border-radius: 60px 60px 24px 24px;
  }
  .tagline-band {
    position: absolute; left: 0; bottom: 0; width: 100%; height: 74px;
    background: var(--cocoa); color: var(--paper);
    display: flex; align-items: center; padding-left: 29px;
    font-weight: 500; font-size: 30px; white-space: nowrap;
  }

  /* Back */
  .card--back { top: 634px; height: 478px; }
  .photo {
    position: absolute; inset: 0;
    background:
      radial-gradient(ellipse 40% 45% at 55% 45%, var(--ginger) 0%, rgba(200,112,46,0.6) 55%, rgba(200,112,46,0) 100%),
      linear-gradient(180deg, var(--soil) 0%, #3b3a2c 22%, var(--meadow) 45%, var(--meadow-light) 70%, var(--meadow) 100%);
  }
  .brand-badge--ghost {
    left: 30px; top: 30px; width: 112px; height: 115px;
    background: rgba(255,255,255,0.35);
  }
  .brand-badge--ghost .brand-badge__name { font-size: 18px; }
  .back-caption {
    position: absolute; left: 0; width: 100%; top: 378px; text-align: center;
    color: var(--cocoa); font-weight: 700; text-transform: uppercase;
    font-size: 29px; line-height: 40px; letter-spacing: -0.5px;
    text-shadow: 1px 1px 0 var(--paper), -1px -1px 0 var(--paper), 1px -1px 0 var(--paper), -1px 1px 0 var(--paper);
  }
  .back-caption span { display: block; }
  .back-caption__tagline { padding-left: 18px; font-size: 30px; }
</style>
</head>
<body>
<main class="canvas">
  <section class="card card--front">
    <div class="brand-badge"><span class="brand-badge__name">Purrlane<br>Nest Co</span></div>
    <h1 class="company-name">PURRLANE NEST CO</h1>
    <ul class="contact">
      <li>www.purrlanenestco.example</li>
      <li>Email: support@purrlanenestco.example</li>
      <li>Phone: +1 (808) 555 0172</li>
    </ul>
    <div class="cat-figure" role="img" aria-label="White silhouette of a sitting cat"></div>
    <div class="tagline-band">Where The Freshest Kitty Sprouts Begin</div>
  </section>

  <section class="card card--back">
    <div class="photo" role="img" aria-label="Photo of a ginger and white cat nibbling fresh green grass"></div>
    <div class="brand-badge brand-badge--ghost"><span class="brand-badge__name">Purrlane<br>Nest Co</span></div>
    <p class="back-caption">
      <span>Purrlane Nest Co</span>
      <span class="back-caption__tagline">Where The Freshest Kitty Sprouts Begin</span>
    </p>
  </section>
</main>
</body>
</html>
```